Business Card Design

I am a classical pilates instructor. I have a home studio, teach out a of a large studio downtown, and teach at on location corporate settings
I like my card to be very simple and clean.
I would like a silhouette of the picture I'm uploading on my design. In the upload section it looks like the picture is cut off and only showing a leg in the air...let me know if you can open up the entire picture.

Industry/Entity Type
Business
Contact Information for Business Card
Moira Kestley Pilates
Certified - The Pilates Center of Harnley
mo.kestley58@postvale.net
615.473.2186

```html
<!DOCTYPE html>
<html lang="en">
<head>
<meta charset="utf-8">
<title>Moira Kestley Pilates – Business Card</title>
<link rel="stylesheet" href="https://fonts.googleapis.com/css2?family=Source+Sans+3:wght@400;600;700&display=swap">
<style>
  :root {
    --backdrop: #e9e6e1;
    --card-white: #f3f2f0;
    --panel-white: #eeedeb;
    --brand-red: #c8202f;
    --ink-dark: #2b2b2b;
    --photo-light: #d9d9d9;
    --photo-dark: #6e6e6e;
  }
  * { box-sizing: border-box; margin: 0; padding: 0; }
  html, body {
    width: 1200px;
    height: 805px;
    overflow: hidden;
    background: var(--backdrop);
    font-family: "Source Sans 3", "Helvetica Neue", Arial, sans-serif;
  }
  .business-card {
    position: absolute;
    left: 120px;
    top: 128px;
    width: 960px;
    height: 548px;
    background: var(--card-white);
    box-shadow: 0 10px 30px rgba(0,0,0,0.18);
    overflow: hidden;
  }
  .card-photo {
    position: absolute;
    inset: 0;
    clip-path: polygon(0 210px, 550px 210px, 640px 548px, 0 548px);
    background: linear-gradient(160deg, var(--photo-light) 0%, #bdbdbd 55%, var(--photo-dark) 100%);
  }
  .card-shapes {
    position: absolute;
    inset: 0;
  }
  .name-block {
    position: absolute;
    left: 48px;
    top: 70px;
    color: #fff;
    white-space: nowrap;
  }
  .name-block .full-name {
    font-size: 38px;
    font-weight: 700;
    letter-spacing: -0.5px;
    line-height: 1;
  }
  .name-block .credential { color: var(--ink-dark); }
  .name-block .studio {
    margin-top: 12px;
    font-size: 21px;
    font-weight: 400;
  }
  .contact-row {
    position: absolute;
    right: 52px;
    display: flex;
    align-items: center;
    gap: 18px;
  }
  .contact-row .contact-text {
    position: relative;
    color: var(--ink-dark);
    padding-bottom: 8px;
    white-space: nowrap;
  }
  .contact-row .contact-text::after {
    content: "";
    position: absolute;
    left: -60px;
    right: -26px;
    bottom: 0;
    height: 2px;
    background: linear-gradient(90deg, rgba(200,32,47,0) 0%, var(--brand-red) 100%);
  }
  .contact-phone { top: 232px; }
  .contact-phone .contact-text { font-size: 30px; font-weight: 400; letter-spacing: 0.5px; }
  .contact-email { top: 312px; }
  .contact-email .contact-text { font-size: 19px; }
  .hex-icon { width: 46px; height: 46px; flex: none; }
</style>
</head>
<body>
  <div class="business-card">
    <div class="card-photo" role="img" aria-label="Black and white photograph of a pilates instructor in a standing split pose on a beach"></div>

    <svg class="card-shapes" viewBox="0 0 960 548" width="960" height="548" aria-hidden="true">
      <polygon points="0,0 640,0 550,210 0,210" fill="var(--brand-red)"/>
      <polygon points="640,0 960,0 960,548 640,548 550,210" fill="var(--panel-white)"/>
      <polyline points="640,0 550,210 640,548" fill="none" stroke="rgba(0,0,0,0.12)" stroke-width="3"/>
    </svg>

    <div class="name-block">
      <div class="full-name">Moira Kestley <span class="credential">Pilates Certified</span></div>
      <div class="studio">The Pilates Center of Harnley</div>
    </div>

    <div class="contact-row contact-phone">
      <span class="contact-text">615.473.2186</span>
      <svg class="hex-icon" viewBox="0 0 46 46" aria-hidden="true">
        <polygon points="13,2 33,2 44,14 44,32 33,44 13,44 2,32 2,14" fill="var(--brand-red)"/>
        <path d="M13 17 q10 -7 20 0 v4 h-5 v-3 q-5 -2 -10 0 v3 h-5z" fill="#fff"/>
        <rect x="15" y="23" width="16" height="10" rx="2" fill="#fff"/>
        <circle cx="23" cy="28" r="2.5" fill="var(--brand-red)"/>
      </svg>
    </div>

    <div class="contact-row contact-email">
      <span class="contact-text">mo.kestley58@postvale.net</span>
      <svg class="hex-icon" viewBox="0 0 46 46" aria-hidden="true">
        <polygon points="13,2 33,2 44,14 44,32 33,44 13,44 2,32 2,14" fill="var(--brand-red)"/>
        <rect x="12" y="13" width="22" height="15" rx="1.5" fill="none" stroke="#fff" stroke-width="2.5"/>
        <rect x="20" y="28" width="6" height="4" fill="#fff"/>
        <rect x="16" y="32" width="14" height="2.5" fill="#fff"/>
      </svg>
    </div>
  </div>
</body>
</html>
```